Tidal Fern Business Cards

We need something new, fun and exciting for business cards. Our current ones are just plain and we need a design that pops. We want name, position held, phone, email on the front, and a 20% discount on the back. I have also uploaded our old business cards creative to see what we are not wanting, and how boring they were and we want something jazzed up from this, cool design and catches people attention.

```html
<!DOCTYPE html>
<html lang="en">
<head>
<meta charset="utf-8">
<title>Tidal Fern Business Cards</title>
<link rel="stylesheet" href="https://fonts.googleapis.com/css2?family=Urbanist:ital,wght@0,400;0,500;0,700;0,800;1,900&display=swap">
<style>
  :root {
    --navy: #2f4b72;
    --coral: #e0706e;
    --coral-soft: #e78583;
    --paper: #efefef;
    --white: #ffffff;
    --backdrop: #c2c2c2;
  }
  * { box-sizing: border-box; margin: 0; padding: 0; }
  html, body { width: 1200px; height: 840px; overflow: hidden; }
  body {
    background: var(--backdrop);
    font-family: "Urbanist", sans-serif;
    position: relative;
  }
  .card {
    position: absolute;
    width: 502px;
    height: 278px;
    overflow: hidden;
  }
  .card--front-light { left: 77px; top: 118px; background: var(--paper); color: var(--navy); }
  .card--front-dark  { left: 77px; top: 455px; background: var(--navy); color: var(--white); }
  .card--back-top    { left: 628px; top: 118px; background: var(--navy); }
  .card--back-bottom { left: 628px; top: 455px; background: var(--navy); }

  /* Front */
  .brand {
    position: absolute;
    left: 30px;
    top: 44px;
    display: flex;
    align-items: center;
    gap: 12px;
  }
  .brand__dot {
    width: 26px; height: 26px;
    border-radius: 50%;
    background: var(--coral);
  }
  .brand__name {
    font-weight: 700;
    font-size: 44px;
    line-height: 1;
    letter-spacing: -0.5px;
  }
  .person {
    position: absolute;
    left: 98px;
    top: 140px;
  }
  .person__name { font-weight: 800; font-size: 22px; line-height: 1.1; }
  .person__role { font-weight: 500; font-size: 14px; margin-top: 2px; }
  .contacts {
    position: absolute;
    left: 97px;
    top: 201px;
    list-style: none;
  }
  .contacts__item {
    display: flex;
    align-items: center;
    gap: 11px;
    font-size: 15px;
    font-weight: 400;
    height: 20px;
  }
  .contacts__item svg { width: 17px; height: 17px; flex: none; }
  .ribbon-art {
    position: absolute;
    left: 306px;
    top: 82px;
    width: 200px;
    height: 200px;
    border-radius: 46% 40% 0 60%;
    background: linear-gradient(150deg, var(--coral) 0%, var(--coral-soft) 100%);
  }

  /* Back */
  .promo-art {
    position: absolute;
    left: 58px;
    top: 22px;
    width: 385px;
    height: 234px;
    border-radius: 60px 26px 40px 30px;
    background: linear-gradient(160deg, var(--coral) 0%, var(--coral-soft) 100%);
  }
  .promo__url {
    position: absolute;
    left: 243px;
    top: 56px;
    font-size: 13px;
    font-weight: 500;
    letter-spacing: 1px;
    color: var(--white);
  }
  .promo__rate {
    position: absolute;
    left: 228px;
    top: 90px;
    font-size: 50px;
    font-weight: 500;
    line-height: 1;
    color: var(--coral);
    -webkit-text-stroke: 2px var(--white);
  }
  .promo__label {
    position: absolute;
    left: 106px;
    top: 138px;
    font-size: 45px;
    font-weight: 900;
    font-style: italic;
    line-height: 1;
    color: var(--white);
    text-shadow: 2px 3px 4px rgba(0, 0, 0, 0.25);
  }
  .promo__brand-box {
    position: absolute;
    left: 236px;
    top: 196px;
    width: 168px;
    height: 44px;
    border-radius: 10px;
    background: var(--white);
    display: flex;
    align-items: center;
    justify-content: center;
  }
  .promo__brand {
    font-size: 28px;
    font-weight: 700;
    color: var(--navy);
    line-height: 1;
  }
</style>
</head>
<body>

  <!-- Front, light -->
  <section class="card card--front-light">
    <div class="brand">
      <span class="brand__dot"></span>
      <span class="brand__name">Tidal Fern</span>
    </div>
    <div class="person">
      <p class="person__name">Maren Holt</p>
      <p class="person__role">President</p>
    </div>
    <ul class="contacts">
      <li class="contacts__item">
        <svg viewBox="0 0 20 20" aria-hidden="true"><circle cx="10" cy="10" r="10" fill="var(--coral)"/><path d="M7 5.5l1.6 2.4-1 1.1a6 6 0 0 0 3.4 3.4l1.1-1 2.4 1.6-.9 1.8c-4.1-.3-7.7-3.9-8-8z" fill="#fff"/></svg>
        <span>555-014-2288</span>
      </li>
      <li class="contacts__item">
        <svg viewBox="0 0 20 20" aria-hidden="true"><circle cx="10" cy="10" r="10" fill="var(--coral)"/><rect x="5" y="6.5" width="10" height="7" rx="1" fill="#fff"/><path d="M5.4 7l4.6 3.6L14.6 7" fill="none" stroke="var(--coral)" stroke-width="1"/></svg>
        <span>maren@tidalfern.com</span>
      </li>
    </ul>
    <div class="ribbon-art" role="img" aria-label="Large coral ribbon heart decoration"></div>
  </section>

  <!-- Front, dark -->
  <section class="card card--front-dark">
    <div class="brand">
      <span class="brand__dot"></span>
      <span class="brand__name">Tidal Fern</span>
    </div>
    <div class="person">
      <p class="person__name">Maren Holt</p>
      <p class="person__role">President</p>
    </div>
    <ul class="contacts">
      <li class="contacts__item">
        <svg viewBox="0 0 20 20" aria-hidden="true"><circle cx="10" cy="10" r="10" fill="var(--coral)"/><path d="M7 5.5l1.6 2.4-1 1.1a6 6 0 0 0 3.4 3.4l1.1-1 2.4 1.6-.9 1.8c-4.1-.3-7.7-3.9-8-8z" fill="#fff"/></svg>
        <span>555-014-2288</span>
      </li>
      <li class="contacts__item">
        <svg viewBox="0 0 20 20" aria-hidden="true"><circle cx="10" cy="10" r="10" fill="var(--coral)"/><rect x="5" y="6.5" width="10" height="7" rx="1" fill="#fff"/><path d="M5.4 7l4.6 3.6L14.6 7" fill="none" stroke="var(--coral)" stroke-width="1"/></svg>
        <span>maren@tidalfern.com</span>
      </li>
    </ul>
    <div class="ribbon-art" role="img" aria-label="Large coral ribbon heart decoration"></div>
  </section>

  <!-- Back, top -->
  <section class="card card--back-top">
    <div class="promo-art" role="img" aria-label="Coral ribbon heart with painted brush strokes"></div>
    <p class="promo__url">WWW.TIDALFERN.COM</p>
    <p class="promo__rate">%20</p>
    <p class="promo__label">DISCOUNT</p>
    <div class="promo__brand-box"><span class="promo__brand">Tidal Fern</span></div>
  </section>

  <!-- Back, bottom -->
  <section class="card card--back-bottom">
    <div class="promo-art" role="img" aria-label="Coral ribbon heart with painted brush strokes"></div>
    <p class="promo__url">WWW.TIDALFERN.COM</p>
    <p class="promo__rate">%20</p>
    <p class="promo__label">DISCOUNT</p>
    <div class="promo__brand-box"><span class="promo__brand">Tidal Fern</span></div>
  </section>

</body>
</html>
```